Plakat für Feinkosthersteller
Zielgruppe
Wir sind ein Feinkosthersteller mit Fokus auf traditionelle schwäbische Produkte, die modern interpretiert und hochwertig hergestellt werden.
Unsere Produkte werden über 24/7-Verkaufsautomaten in Berlin vertrieben.
Unsere Zielgruppe sind junge Familien, zugezogene Schwaben in Berlin sowie Berlinerinnen und Berliner, die längere Zeit im Schwabenland verbracht haben und eine emotionale Verbindung zu schwäbischen Spezialitäten haben.
Die Marke verbindet Heimatgefühl, Qualität und ehrliche Küche mit einem urbanen, zeitgemäßen Auftritt.
Aufgabenstellung
Die zentrale Botschaft des Automaten ist „Heimat auf Knopfdruck“.
Der Verkaufsautomat soll Heimatgefühl, Vertrautheit und Qualität vermitteln – gleichzeitig aber modern, urban und aufmerksamkeitsstark sein.
Das Design soll so auffällig sein, dass man beim Vorbeigehen stehen bleibt und neugierig wird. Der Automat ist 24/7 zugänglich, entsprechend darf und soll er visuell präsent und markant sein.
Pflichtelemente:
– Unser Logo inklusive Korn & Kruste (wird hochgeladen)
– Der Slogan: „Heimat auf Knopfdruck“
Farbwelt:
– Orientierung an den Farben Baden-Württembergs: Gelb und Schwarz
– Gerne kräftig und kontrastreich, aber hochwertig (nicht billig oder grell)
Stil & Wirkung:
– modern, urban, selbstbewusst
– kein Kitsch, keine Trachten- oder Folkloreoptik
– eher zeitgemäß als rustikal
– emotionale Verbindung zu schwäbischer Heimat, aber klar in Berlin verortet
Format & Anwendung:
– Design für die Außenfläche eines Verkaufsautomaten (24/7 sichtbar)
– Bitte so gestalten, dass das Layout auch aus einigen Metern Entfernung gut wirkt

```html
<!DOCTYPE html>
<html lang="de">
<head>
<meta charset="utf-8">
<title>Korn &amp; Kruste – Automatengestaltung</title>
<link rel="stylesheet" href="https://fonts.googleapis.com/css2?family=Anton&family=Oswald:wght@600;700&family=Roboto+Condensed:wght@400&display=swap">
<style>
  :root{
    --page:#e9e9e9;
    --board:#000000;
    --yellow:#ecbb62;
    --ink:#111111;
    --machine:#1d1c1c;
    --window:#3b3737;
    --edge:#8a8a8a;
    --label:#ffffff;
    --illustration:#6b5327;
  }
  html,body{margin:0;padding:0;width:849px;height:1200px;overflow:hidden;background:var(--page);}
  .board{position:absolute;left:20px;top:317px;width:809px;height:566px;background:var(--board);}
  .side{position:absolute;top:55px;width:195px;height:386px;}
  .side--left{left:59px;}
  .side--right{left:552px;}
  .front{position:absolute;left:305px;top:55px;width:198px;height:401px;}
  .label{position:absolute;top:468px;font-family:"Roboto Condensed",sans-serif;font-size:15px;color:var(--label);}
  .label--left{left:59px;}
  .label--front{left:366px;}
  .label--right{right:62px;}
  .headline{font-family:"Anton",sans-serif;fill:var(--ink);}
  .headline--inverse{fill:var(--yellow);}
  .tagline{font-family:"Oswald",sans-serif;font-weight:700;fill:var(--yellow);}
  .brand{font-family:"Oswald",sans-serif;font-weight:700;fill:var(--yellow);}
</style>
</head>
<body>
<div class="board">

  <svg class="side side--left" viewBox="0 0 195 386" aria-label="Linke Seitenfläche">
    <rect width="195" height="386" fill="var(--yellow)"/>
    <rect x="62" y="11" width="68" height="57" fill="var(--ink)"/>
    <text class="brand" x="96" y="36" text-anchor="middle" font-size="12">KORN</text>
    <text class="brand" x="96" y="50" text-anchor="middle" font-size="10">&amp;</text>
    <text class="brand" x="96" y="63" text-anchor="middle" font-size="12">KRUSTE</text>
    <g stroke="var(--ink)" stroke-width="1.4">
      <line x1="34" y1="166" x2="34" y2="176"/><line x1="34" y1="202" x2="34" y2="212"/>
      <line x1="6" y1="189" x2="18" y2="189"/><line x1="16" y1="173" x2="22" y2="178"/>
      <line x1="16" y1="205" x2="22" y2="200"/><line x1="52" y1="205" x2="46" y2="200"/>
    </g>
    <text class="headline" x="45" y="180" font-size="31" textLength="93" lengthAdjust="spacingAndGlyphs">HEIMAT</text>
    <circle cx="34" cy="189" r="13" fill="var(--ink)"/>
    <text class="headline headline--inverse" x="34" y="195" text-anchor="middle" font-size="14">auf</text>
    <text class="headline" x="50" y="204" font-size="23" textLength="140" lengthAdjust="spacingAndGlyphs">KNOPFDRUCK</text>
    <polygon points="0,259 195,310 195,381 0,330" fill="var(--ink)"/>
    <rect x="49" y="225" width="93" height="76" rx="30" fill="var(--illustration)" role="img" aria-label="Illustration dampfender Maultaschen"/>
    <g transform="rotate(14.7 0 259)">
      <text class="tagline" x="10" y="296" font-size="13" textLength="176" lengthAdjust="spacingAndGlyphs">SCHWÄBISCHE SPEZIALITÄTEN</text>
      <text class="tagline" x="76" y="320" font-size="22">24/7</text>
    </g>
  </svg>

  <svg class="front" viewBox="0 0 198 401" aria-label="Vorderseite">
    <rect x="0.5" y="0.5" width="197" height="400" fill="var(--machine)" stroke="var(--edge)" stroke-width="1"/>
    <rect x="23.5" y="19" width="144" height="242" fill="var(--window)"/>
    <text class="tagline" x="95" y="276" text-anchor="middle" font-size="9" font-weight="600">Hier kommt Heimat raus!</text>
    <rect x="48" y="282" width="95" height="37" fill="none" stroke="var(--yellow)" stroke-width="1.5"/>
    <rect x="76" y="340" width="39" height="33" fill="none" stroke="var(--yellow)" stroke-width="1"/>
    <text class="brand" x="95.5" y="354" text-anchor="middle" font-size="7.5">KORN &amp;</text>
    <text class="brand" x="95.5" y="365" text-anchor="middle" font-size="7.5">KRUSTE</text>
    <text class="tagline" x="17" y="391" font-size="9.5" textLength="128" lengthAdjust="spacingAndGlyphs">SCHWÄBISCHE SPEZIALITÄTEN</text>
    <text class="tagline" x="149" y="392" font-size="13">24/7</text>
  </svg>

  <svg class="side side--right" viewBox="0 0 195 386" aria-label="Rechte Seitenfläche">
    <rect width="195" height="386" fill="var(--yellow)"/>
    <rect x="63" y="11" width="68" height="57" fill="var(--ink)"/>
    <text class="brand" x="97" y="36" text-anchor="middle" font-size="12">KORN</text>
    <text class="brand" x="97" y="50" text-anchor="middle" font-size="10">&amp;</text>
    <text class="brand" x="97" y="63" text-anchor="middle" font-size="12">KRUSTE</text>
    <text class="headline" x="20" y="177" font-size="36" textLength="110" lengthAdjust="spacingAndGlyphs">HEIMAT</text>
    <circle cx="143" cy="159" r="13" fill="var(--ink)"/>
    <text class="headline headline--inverse" x="143" y="165" text-anchor="middle" font-size="14">auf</text>
    <text class="headline" x="25" y="205" font-size="27" textLength="154" lengthAdjust="spacingAndGlyphs">KNOPFDRUCK</text>
    <polygon points="0,314 195,260 195,330 0,377" fill="var(--ink)"/>
    <rect x="52" y="228" width="92" height="74" rx="30" fill="var(--illustration)" role="img" aria-label="Illustration dampfender Maultaschen"/>
    <g transform="rotate(-15.5 0 314)">
      <text class="tagline" x="-5" y="350" font-size="13" textLength="182" lengthAdjust="spacingAndGlyphs">SCHWÄBISCHE SPEZIALITÄTEN</text>
      <text class="tagline" x="68" y="373" font-size="22">24/7</text>
    </g>
  </svg>

  <div class="label label--left">Linke Seite</div>
  <div class="label label--front">Vorderseite</div>
  <div class="label label--right">Rechte Seite</div>
</div>
</body>
</html>
```